Brochure Design Project

We require a great design for a brochure that we will be giving to people who are interested in buying one of our franchises.
From this brochure they will need to get the feel of a succesful business that they would love to be a part of

Please also include the title
Become Part of a National Sign Manufacturing Company

Hi Everyone
Does anyone have any designs that they are adding because we will be making our descision in approx an hour

Thank you

Industry/Entity Type

Business

Requirements
Must have
• This brochure must be 2 page A4 (front and back)
can be either portrait or landscape orientation (which ever works best with the design)
Must have our logo and colours
Must include all the information provided in the Word Document
Nice to have
• Can include images if it works with the design
can use either stock images of profesionals or see our website
www.kelvorasigns.com.au for some images

```html
<!DOCTYPE html>
<html lang="en">
<head>
<meta charset="utf-8">
<title>Kelvora – Franchise Brochure</title>
<link href="https://fonts.googleapis.com/css2?family=Roboto+Condensed:wght@400;700&family=Oswald:wght@600&display=swap" rel="stylesheet">
<style>
:root{
  --blue:#1b86c6;--blue-dark:#1d3f8f;--orange:#e6a01c;--green:#6bb33c;--red:#e0282a;
  --purple:#8e1b8c;--grey:#6f6f6f;--ink:#2b2b2b;--divider:#8a8a8a;
}
*{margin:0;padding:0;box-sizing:border-box}
html,body{width:1200px;height:849px;overflow:hidden;background:#fff}
body{position:relative;font-family:"Roboto Condensed",Arial,sans-serif;font-weight:700}
.page{position:absolute;top:0;height:849px;background:#fff;overflow:hidden}
.page--left{left:0;width:595px}
.page--right{left:603px;width:597px}
.spine{position:absolute;left:595px;top:0;width:8px;height:849px;background:linear-gradient(90deg,#fff,var(--divider) 40%,#fff)}
.abs{position:absolute}
.logo{display:flex;align-items:center;gap:8px;color:var(--grey);font-size:38px;letter-spacing:1px}
.logo__dot{width:22px;height:22px;border-radius:50%;background:var(--blue)}
.rule{height:3px;background:#bdbdbd}
.intro{font-size:6.4px;line-height:7.6px;width:185px}
.icon-label{font-size:9px;text-align:center;width:80px}
.pin-label{font-family:"Oswald",Impact,sans-serif;font-weight:600;text-align:center;line-height:.95}
.txt{font-size:10.3px;line-height:14.2px}
.bullets{list-style:none}
.bullets li{padding-left:14px;text-indent:-9px}
.bullets li::before{content:"• "}
.heading{color:#666;margin-top:12px}
</style>
</head>
<body>

<section class="page page--left">
  <svg class="abs" style="left:290px;top:0" width="305" height="135" viewBox="0 0 305 135" aria-hidden="true">
    <polygon points="10,0 60,0 195,135 145,135" fill="#e4e8f3"/>
    <polygon points="60,0 110,0 230,120 195,135" fill="#c5cde6"/>
    <polygon points="110,0 160,0 260,100 230,120" fill="#9ea9d4"/>
    <polygon points="160,0 210,0 285,75 260,100" fill="#6e7fc0"/>
    <polygon points="210,0 260,0 305,45 305,55 285,75" fill="#4a5fb0"/>
    <polygon points="260,0 305,0 305,45" fill="var(--blue-dark)"/>
  </svg>

  <div class="abs logo" style="left:18px;top:38px"><span class="logo__dot"></span>KELVORA</div>
  <div class="abs rule" style="left:60px;top:76px;width:345px"></div>

  <svg class="abs" style="left:50px;top:104px" width="36" height="36" aria-hidden="true"><circle cx="18" cy="18" r="18" fill="#d4494a"/><circle cx="18" cy="13" r="5" fill="#fff"/><path d="M9 28a9 8 0 0 1 18 0z" fill="#fff"/></svg>
  <div class="abs icon-label" style="left:28px;top:150px;color:var(--red)">How we began</div>
  <p class="abs intro" style="left:116px;top:99px;color:var(--red)">Our long history in the signage industry has spawned a fresh outlook on how we do business and because our core business is working for brokers we are able to save on costs such as advertising and sales reps, in house designers, high exposure sales locations and the list goes on. All of these savings are passed on</p>

  <svg class="abs" style="left:332px;top:102px" width="36" height="36" aria-hidden="true"><circle cx="18" cy="18" r="18" fill="var(--orange)"/><rect x="12" y="10" width="12" height="16" fill="#fff"/><path d="M14 15h8M14 18h8M14 21h8" stroke="var(--orange)"/></svg>
  <div class="abs icon-label" style="left:310px;top:152px;color:var(--orange)">Our Work</div>
  <p class="abs intro" style="left:395px;top:97px;color:var(--orange)">From simple site audits to large scale rebrands we are capable of any form of signage. With in-house fabrication of steel, aluminium and acrylic and also equipment such as printers, laminators, cnc and even our latest edition FDM 3D Print</p>

  <svg class="abs" style="left:50px;top:180px" width="36" height="36" aria-hidden="true"><circle cx="18" cy="18" r="18" fill="#2f7fb5"/><path d="M18 26l-7-7a4 4 0 0 1 7-5 4 4 0 0 1 7 5z" fill="#fff"/></svg>
  <div class="abs icon-label" style="left:33px;top:226px;color:#2f7fb5">Phylosophy</div>
  <p class="abs intro" style="left:116px;top:181px;color:#2f7fb5">Never Let Them Down. As a result of primarily working for a select few brokers our reliability and workmanship is paramount to our success and the sustainability of this company which is why we only strive for the absolute best from all our staff and management</p>

  <svg class="abs" style="left:332px;top:182px" width="36" height="36" aria-hidden="true"><circle cx="18" cy="18" r="18" fill="#7fb33a"/><rect x="10" y="12" width="16" height="12" fill="#fff"/><path d="M10 12l8 7 8-7" stroke="#7fb33a" fill="none"/></svg>
  <div class="abs icon-label" style="left:310px;top:226px;color:#7fb33a;font-size:7px">Get in Touch</div>
  <p class="abs intro" style="left:395px;top:182px;color:#7fb33a">To start benefiting from our fresh approach please give us call, drop us an email or just say our name 3 times, OK maybe not that last one. Whichever way you wish we will be happy to hear from you.</p>

  <svg class="abs" style="left:30px;top:270px" width="220" height="190" viewBox="0 0 220 190" aria-hidden="true">
    <defs><linearGradient id="gBlue" x1="0" y1="0" x2="1" y2="1"><stop offset="0" stop-color="#7fd3f2"/><stop offset="1" stop-color="#1478b4"/></linearGradient></defs>
    <g transform="rotate(-28 90 92)"><path d="M200,92 L134.5,38 A70,70 0 1 0 134.5,146 Z" fill="url(#gBlue)"/></g>
    <circle cx="90" cy="92" r="56" fill="#fff"/>
  </svg>
  <div class="abs pin-label" style="left:58px;top:347px;width:122px;font-size:19px;color:#1b6fa6">OPERTUNITY</div>
  <p class="abs txt" style="left:243px;top:293px;width:290px;color:var(--blue)">An exciting opportunity exists for 7 people to become part of a national sign manufacturing company servicing big name clientele on a national scale. A successful applicant will receive their own State territory branch to operate a sign manufacturing and installation service to our existing clientele. This will be strictly limited to 1 franchise sold per state and if the operator chooses or feels they can better service our clients with multiple outlets within their state then they are at liberty to do so without any further fees incurred.</p>

  <svg class="abs" style="left:25px;top:495px" width="140" height="100" viewBox="0 0 200 185" aria-hidden="true">
    <defs><linearGradient id="gGreen" x1="0" y1="0" x2="1" y2="1"><stop offset="0" stop-color="#a4e28a"/><stop offset="1" stop-color="#2e9b3a"/></linearGradient></defs>
    <g transform="rotate(-25 80 92)"><path d="M190,92 L124.5,38 A70,70 0 1 0 124.5,146 Z" fill="url(#gGreen)"/></g>
    <circle cx="80" cy="92" r="56" fill="#fff"/>
  </svg>
  <div class="abs pin-label" style="left:42px;top:530px;width:60px;font-size:15px;color:var(--green)">WHAT<br>YOU<br>GET</div>
  <ul class="abs txt bullets" style="left:152px;top:472px;width:420px;color:var(--green)">
    <li>You will receive your own State to operate and fulfil all orders within that state</li>
    <li>You can have as many manufacturing facilities you feel are needed to efficiently operate within your state and the best part is that you can grow this over time.</li>
    <li>Operating Procedures and software including quoting systems and pricing structure</li>
    <li>Pre-existing clientele we have been operating since 2006 and have a national network that is growing by the day</li>
    <li>National website and number</li>
    <li>Marketing and new client introduction</li>
    <li>Benefits of being part of a national team that is capable of servicing national clients that would not be possible to service otherwise</li>
    <li>The benefits of this business are growing daily and we have not even scratched the surface of its full potential more and more clients are realising just how much they can benefit from using our services.</li>
  </ul>

  <svg class="abs" style="left:25px;top:690px" width="140" height="100" viewBox="0 0 200 185" aria-hidden="true">
    <defs><linearGradient id="gRed" x1="0" y1="0" x2="1" y2="1"><stop offset="0" stop-color="#f08a8a"/><stop offset="1" stop-color="#c41a1a"/></linearGradient></defs>
    <g transform="rotate(-30 80 92)"><path d="M190,92 L124.5,38 A70,70 0 1 0 124.5,146 Z" fill="url(#gRed)"/></g>
    <circle cx="80" cy="92" r="56" fill="#fff"/>
  </svg>
  <div class="abs pin-label" style="left:42px;top:725px;width:60px;font-size:15px;color:var(--red)">WHAT<br>YOU<br>NEED</div>
  <div class="abs txt" style="left:172px;top:657px;width:408px;color:var(--red)">
    <p>To be successful in ensuring your position within our team you will need to have had experience within the signage industry, have great communication skills and have a good positive attitude towards owning and running a successful business.</p>
    <p style="margin-top:14px">Under no circumstances can you own or be in any way affiliated with another sign company and own a Kelvora branch you can however apply if you are closing or exiting (or intending to exit if successful)</p>
    <p style="margin-top:14px">Some working capital will be needed and this will obviously vary depending on the size of the initial manufacturing setup but a minimum of $20,000 would be advised.<br>A Once off purchase price of your territory will cost $45,000.<br>A suitable place of business, at a minimum this will consist of small office area and ideally 200sqm or more of workshop space</p>
  </div>
</section>

<div class="spine"></div>

<section class="page page--right">
  <svg class="abs" style="left:110px;top:-20px" width="520" height="560" aria-hidden="true">
    <circle cx="330" cy="220" r="210" fill="#eef7fc"/>
    <circle cx="330" cy="220" r="120" fill="#fff"/>
  </svg>

  <svg class="abs" style="left:-4px;top:215px" width="230" height="170" viewBox="0 0 220 185" aria-hidden="true">
    <path d="M200,92 L134.5,38 A70,70 0 1 0 134.5,146 Z" fill="url(#gBlue)"/>
    <circle cx="90" cy="92" r="56" fill="#fff"/>
  </svg>
  <div class="abs pin-label" style="left:20px;top:268px;width:100px;font-size:25px;color:#1b6fa6">Our<br>Clients</div>

  <div class="abs txt" style="left:194px;top:36px;width:390px;color:var(--blue)">
    <p>Our clients are franchises, shopfitters, architects, designers, brokers, multisite organisations and anyone who is ordering signs on a regular basis. We have targeted this clientele for the obvious reasons of continuous work and in return our clients receive:</p>
    <p class="heading">Competitive Pricing</p>
    <p>The reason you will be able to offer competitive pricing is because you will not have to waste time and money on things like in-house design, advertising, sales reps high exposure sales locations and the list goes on All of these savings are passed on to our clients and for this reason we remain number 1 choice time and time again.</p>
    <p class="heading">Consistency and Reliability</p>
    <p>We have systems in place to ensure consistency and reliability across branches by adhering to a minimum standards and code of conduct policy which our customers can view at any time which outlines things such as standard material specifications, warranty periods, standard turnaround times, standard pricing schedules and more, to add to all this the operating systems and software we use ensure reliable and familiar interaction with our clients no matter which branch they are dealing with.</p>
    <p class="heading">Ease of Use</p>
    <p>Just think about it one of the roles of an operations manager of a large company is the organisation and ordering of all the signage requirements for 45 different locations across Australia. Whilst at one of the locations in NSW he notices that the front window graphics have been damaged by graffiti, He calls the NSW Kelvora branch and begins the process of ordering some replacement window graphics and chooses to freshen up the graphics with some new designs that had been recently added to the brands new style guide, now he already knows that he is getting a quality product that has been specified in the minimum standards and code of conduct policy and he already knows the cost of the product because the pricing structure has also been outlined he knows that the branch has access to the customers data base with style guide so he knows they have the artwork files plus he knows that the colours will be correct because all that info is in the customers file, so in other words he know how easy it is to order from the Kelvora branch. Then one week later he is in Victoria visiting another one of the 45 locations and would you believe he notices that yet again the windows have been vandalised and yes another opportunity to refresh the images so off course he call the Kelvora VIC office and begins the process again and all he has to do is say we want the graphics exactly the same as the ones done 2 weeks ago at the other location, Easy</p>
  </div>

  <svg class="abs" style="left:80px;top:597px" width="110" height="70" viewBox="0 0 200 130" aria-hidden="true">
    <defs><linearGradient id="gPink" x1="0" y1="0" x2="1" y2="1"><stop offset="0" stop-color="#f29bdc"/><stop offset="1" stop-color="#b0168f"/></linearGradient></defs>
    <path d="M190,65 L124.5,11 A70,70 0 1 0 124.5,119 Z" fill="url(#gPink)"/>
    <circle cx="80" cy="65" r="54" fill="#fff"/>
  </svg>
  <div class="abs pin-label" style="left:96px;top:622px;width:56px;font-size:15px;color:var(--purple)">COST</div>
  <ul class="abs txt bullets" style="left:190px;top:618px;width:300px;color:var(--purple);line-height:13px">
    <li>$45,000 ONCE OFF PURCHASE PRICE FOR YOUR TERRITORY</li>
    <li>7% OF SALES</li>
  </ul>

  <svg class="abs" style="left:80px;top:685px" width="110" height="70" viewBox="0 0 200 130" aria-hidden="true">
    <defs><linearGradient id="gGrey" x1="0" y1="0" x2="1" y2="1"><stop offset="0" stop-color="#c9c9c9"/><stop offset="1" stop-color="#555"/></linearGradient></defs>
    <path d="M190,65 L124.5,11 A70,70 0 1 0 124.5,119 Z" fill="url(#gGrey)"/>
    <circle cx="80" cy="65" r="54" fill="#fff"/>
  </svg>
  <div class="abs pin-label" style="left:92px;top:713px;width:66px;font-size:11px;color:var(--ink)">CONTGACT</div>
  <div class="abs txt" style="left:198px;top:698px;color:var(--ink);line-height:14px">
    <div><span style="display:inline-block;width:48px">PH:</span>1300 555 014</div>
    <div><span style="display:inline-block;width:40px">EMAIL:</span>ACCOUNTS@KELVORASIGNS.COM.AU</div>
    <div><span style="display:inline-block;width:48px">WEB:</span>WWW.KELVORASIGNS.COM.AU</div>
  </div>

  <div class="abs logo" style="left:370px;top:780px"><span class="logo__dot"></span>KELVORA</div>
</section>

</body>
</html>
```